** Wanted ** Wordpress web design for scaffolding rental and construction company

We need a website design and must be functional to show a basic overview of what our company offers as a service. We have a domain name and a logo but we need web design. This web site should have another scaffolding rental page for construction and renovation as well as a quote section where customers can enter their personal information and also upload photos. The site% 26quot; www.corvithane.com% 26quot; should be intuitive, clear and classy ... The logo must be found on the site in several ways.

Target Market(s)

Professional and no professional

Coding

Coded - Design and coding required

Number of Pages Required

3 page

Font styles to use
Serif
Sans Serif
Decorative
Script

Requirements
Must have
• Our logo
Nice to have
• Slogan:% 26quot; The height% 26 # 224; port% 26 # 233; e hand% 26quot;

```html
<!DOCTYPE html>
<html lang="en">
<head>
<meta charset="utf-8">
<title>Corvithane – Scaffolding for Building Construction</title>
<link href="https://fonts.googleapis.com/css2?family=Montserrat:wght@300;400;500;600;700;800&display=swap" rel="stylesheet">
<style>
:root{
  --orange:#f7931e;
  --navy:#0b1824;
  --navy-2:#1c232b;
  --blue:#1e8fe3;
  --ink:#1b2633;
  --text:#444b52;
  --white:#ffffff;
}
*{box-sizing:border-box;margin:0;padding:0}
html,body{width:1200px;height:4444px;overflow:hidden}
body{font-family:'Montserrat',sans-serif;color:var(--text);background:var(--white)}
section,header,footer,nav{position:relative;display:block;width:1200px}
.container{position:absolute;left:158px;width:886px}
.brand{display:flex;align-items:center;gap:8px;font-weight:700;font-size:15px;letter-spacing:1.5px;color:var(--orange)}
.brand-mark{width:14px;height:14px;background:var(--orange)}

/* top bar */
.topbar{height:56px;font-size:11.5px;color:#333}
.topbar .item{position:absolute;top:18px;display:flex;align-items:center;gap:6px}
.topbar svg{width:12px;height:12px;fill:#333}

/* nav */
.nav{height:96px;background:var(--navy-2)}
.nav .brand{position:absolute;left:159px;top:40px}
.nav ul{position:absolute;right:126px;top:0;height:96px;display:flex;align-items:center;gap:40px;list-style:none}
.nav li{font-size:13px;font-weight:500;color:var(--white);letter-spacing:.5px}
.nav li.active{color:var(--orange)}

/* hero */
.hero{height:417px;overflow:hidden}
.hero-photo{position:absolute;inset:0;background:linear-gradient(100deg,#c8d4de 0%,#e5e9ee 40%,#b9b3a6 65%,#8f8677 100%)}
.hero-shape{position:absolute;inset:0;width:1200px;height:417px}
.hero h1{position:absolute;left:155px;top:134px;font-size:48px;line-height:52px;color:var(--white);font-weight:700;letter-spacing:1px}
.hero h1 .thin{font-weight:300}
.hero h1 .dark{color:var(--navy);font-weight:800}
.slider-dots{position:absolute;left:159px;top:382px;display:flex;gap:4px}
.slider-dots span{width:5px;height:5px;border-radius:50%;background:var(--white)}

/* section titles */
.section-title{position:absolute;left:0;width:1200px;text-align:center;font-size:34px;font-weight:700;color:var(--ink);letter-spacing:1px}

/* services */
.services{height:1086px}
.services .section-title{top:66px}
.service-grid{top:121px;display:grid;grid-template-columns:repeat(3,285px);column-gap:15px;row-gap:0}
.service-card{height:465px}
.service-img{width:285px;height:284px;border:4px solid var(--white);box-shadow:0 1px 6px rgba(0,0,0,.3)}
.service-card h3{margin:14px 0 0 2px;font-size:18px;font-weight:500;color:#2a2f35}
.service-card p{margin:10px 2px 0;font-size:12px;line-height:19px;color:#555}
.more{display:flex;align-items:center;gap:4px;margin:8px 2px 0;font-size:11.5px;font-weight:700;color:var(--ink)}
.more svg{width:10px;height:10px;stroke:var(--ink);fill:none;stroke-width:1.6}

/* about */
.about{height:635px;background:linear-gradient(90deg,#f9f9f9,#ececec)}
.about-photo{position:absolute;left:0;top:0;width:536px;height:635px;background:linear-gradient(180deg,#cfd9e4 0%,#e8ecef 30%,#4f8a63 50%,#355c45 70%,#5b5650 100%)}
.about-body{position:absolute;left:593px;top:92px;width:445px}
.about-body h2{font-size:33px;font-weight:700;color:var(--ink);letter-spacing:1px;margin-bottom:14px}
.about-body p{font-size:12px;line-height:18.7px;color:#444;margin-bottom:10px}
.stats{position:absolute;left:536px;top:541px;width:664px;height:94px;display:flex}
.stat{display:flex;flex-direction:column;align-items:center;justify-content:center;color:var(--white)}
.stat strong{font-size:33px;font-weight:700;line-height:36px}
.stat span{font-size:16px;letter-spacing:.5px}
.stat.blue{width:254px;background:var(--blue)}
.stat.dark{flex:1;background:var(--navy)}

/* projects */
.projects{height:827px}
.projects .section-title{top:66px}
.project-grid{top:137px;height:560px}
.project{position:absolute}
.project-img{border:4px solid var(--white);box-shadow:0 1px 6px rgba(0,0,0,.3)}
.project h3{font-size:19px;font-weight:600;color:#2a2f35;margin-top:8px}
.btn{position:absolute;left:515px;width:170px;height:53px;background:var(--orange);color:var(--white);font-size:16px;font-weight:700;display:flex;align-items:center;justify-content:center;letter-spacing:.5px}
.projects .btn{top:701px}

/* testimonials */
.testimonials{height:555px;background:var(--navy)}
.testimonials .section-title{top:69px;color:var(--white)}
.quote-card{position:absolute;top:153px;width:290px;text-align:center;color:#b9c0c6}
.avatar{width:108px;height:108px;margin:0 auto;border-radius:50%;border:3px solid var(--orange);background:linear-gradient(180deg,#e7e3df,#c9c1b8)}
.quote-card .name{margin-top:12px;font-size:13px;line-height:19px}
.quote-card .mark{font-size:44px;font-weight:700;color:var(--white);line-height:30px;margin-top:6px;font-style:italic}
.quote-card p{font-size:12.5px;line-height:19px;margin-top:6px;padding:0 6px}
.test-dots{position:absolute;top:468px;left:580px;display:flex;gap:12px}
.test-dots span{width:7px;height:7px;border-radius:50%;background:var(--white)}
.test-dots span.on{background:var(--orange)}

/* call to action */
.cta{height:366px}
.cta h2{position:absolute;top:96px;width:1200px;text-align:center;font-size:32px;line-height:44px;font-weight:700;color:var(--ink);letter-spacing:1px}
.cta .btn{top:209px}

/* footer */
.footer{height:406px;background:var(--navy-2);color:#c9ced3;font-size:12.5px}
.footer .brand{position:absolute;left:159px;top:50px}
.footer-about{position:absolute;left:159px;top:123px;width:270px;line-height:20.5px}
.footer h4{font-size:14px;font-weight:600;color:var(--white);letter-spacing:.5px}
.footer-col{position:absolute;top:69px}
.footer-col ul{list-style:none;margin-top:20px}
.footer-services li{display:flex;align-items:center;gap:18px;height:33px}
.footer-services li::before{content:"";width:5px;height:5px;border-radius:50%;background:var(--white)}
.footer-contact li{display:flex;gap:12px;margin-bottom:22px;line-height:19px}
.footer-contact svg{width:16px;height:16px;flex:none;fill:var(--white)}
.socials{display:flex;gap:8px}
.socials span{width:32px;height:32px;border-radius:50%;background:var(--white)}
.copyright{position:absolute;top:367px;width:1200px;text-align:center;font-size:12.5px;color:#c9ced3}
</style>
</head>
<body>

<header class="topbar">
  <div class="item" style="left:158px">
    <svg viewBox="0 0 24 24"><path d="M6.6 10.8a15 15 0 0 0 6.6 6.6l2.2-2.2a1 1 0 0 1 1-.25 11.4 11.4 0 0 0 3.6.57 1 1 0 0 1 1 1V20a1 1 0 0 1-1 1A17 17 0 0 1 3 4a1 1 0 0 1 1-1h3.5a1 1 0 0 1 1 1c0 1.25.2 2.45.57 3.6a1 1 0 0 1-.25 1z"/></svg>
    555.014.2236
  </div>
  <div class="item" style="left:323px">
    <svg viewBox="0 0 24 24"><path d="M2 5h20v14H2zm2 2v.5l8 5 8-5V7z"/></svg>
    info@corvithane.com
  </div>
  <div class="item" style="left:732px">
    <svg viewBox="0 0 24 24"><path d="M12 2a7 7 0 0 0-7 7c0 5 7 13 7 13s7-8 7-13a7 7 0 0 0-7-7zm0 9.5A2.5 2.5 0 1 1 12 6.5a2.5 2.5 0 0 1 0 5z"/></svg>
    Brightrail Scaffold &amp; Ladders | 4180 Merrow Lane ,NZ
  </div>
</header>

<nav class="nav">
  <div class="brand"><span class="brand-mark"></span>CORVITHANE</div>
  <ul>
    <li class="active">HOME</li>
    <li>SERVICES</li>
    <li>LATEST PROJECT</li>
    <li>TESTIMONIAL</li>
    <li>CONTACT US</li>
  </ul>
</nav>

<section class="hero">
  <div class="hero-photo" role="img" aria-label="Photo of a high-rise under construction with tower cranes and scaffolding"></div>
  <svg class="hero-shape" viewBox="0 0 1200 417" preserveAspectRatio="none">
    <polygon points="0,0 640,0 250,417 0,417" fill="#f7931e" opacity=".92"/>
    <polygon points="640,0 700,0 310,417 250,417" fill="#f7931e" opacity=".55"/>
  </svg>
  <h1>SCAFFOLDING<br><span class="thin">for </span><span class="dark">BUILDING</span><br><span class="thin">Construction</span></h1>
  <div class="slider-dots"><span></span><span></span><span></span><span></span><span></span></div>
</section>

<section class="services">
  <h2 class="section-title">OUR SERVICES</h2>
  <div class="container service-grid">
    <article class="service-card">
      <div class="service-img" role="img" aria-label="Photo of three workers in hard hats reviewing plans" style="background:linear-gradient(180deg,#9aa1a6,#e08a2e 70%,#4b4f55)"></div>
      <h3>Formwork Systems</h3>
      <p>It is a long established fact that a reader will be distracted by the readable content of a page when looking at its layout.</p>
      <div class="more">More Information <svg viewBox="0 0 10 10"><path d="M1 1l4 4-4 4M5 1l4 4-4 4"/></svg></div>
    </article>
    <article class="service-card">
      <div class="service-img" role="img" aria-label="Photo of a dense scaffolding frame" style="background:linear-gradient(180deg,#e6e8ea,#b8bcc0 60%,#d9d4c9)"></div>
      <h3>Scaffolding Systems</h3>
      <p>It is a long established fact that a reader will be distracted by the readable content of a page when looking at its layout.</p>
      <div class="more">More Information <svg viewBox="0 0 10 10"><path d="M1 1l4 4-4 4M5 1l4 4-4 4"/></svg></div>
    </article>
    <article class="service-card">
      <div class="service-img" role="img" aria-label="Photo of an engineer holding a building model" style="background:linear-gradient(160deg,#c9c2b8,#8a8f98 55%,#3d5b8a)"></div>
      <h3>Civil Engineering Solutions</h3>
      <p>It is a long established fact that a reader will be distracted by the readable content of a page when looking at its layout.</p>
      <div class="more">More Information <svg viewBox="0 0 10 10"><path d="M1 1l4 4-4 4M5 1l4 4-4 4"/></svg></div>
    </article>
    <article class="service-card">
      <div class="service-img" role="img" aria-label="Photo of workers on scaffolding inside a building" style="background:linear-gradient(180deg,#d7d9db,#a9adb1 60%,#7d7a72)"></div>
      <h3>Cleaning &amp; Repairs</h3>
      <p>It is a long established fact that a reader will be distracted by the readable content of a page when looking at its layout.</p>
      <div class="more">More Information <svg viewBox="0 0 10 10"><path d="M1 1l4 4-4 4M5 1l4 4-4 4"/></svg></div>
    </article>
    <article class="service-card">
      <div class="service-img" role="img" aria-label="Photo of two site supervisors inspecting a building" style="background:linear-gradient(180deg,#dfe3e6,#8e9aa8 50%,#2b3a52)"></div>
      <h3>Field Services</h3>
      <p>It is a long established fact that a reader will be distracted by the readable content of a page when looking at its layout.</p>
      <div class="more">More Information <svg viewBox="0 0 10 10"><path d="M1 1l4 4-4 4M5 1l4 4-4 4"/></svg></div>
    </article>
    <article class="service-card">
      <div class="service-img" role="img" aria-label="Photo of a blue steel scaffolding grid from above" style="background:linear-gradient(150deg,#d4d8dc,#7d97b3 55%,#5d6a78)"></div>
      <h3>Rental Parks &amp; Distribution</h3>
      <p>It is a long established fact that a reader will be distracted by the readable content of a page when looking at its layout.</p>
      <div class="more">More Information <svg viewBox="0 0 10 10"><path d="M1 1l4 4-4 4M5 1l4 4-4 4"/></svg></div>
    </article>
  </div>
</section>

<section class="about">
  <div class="about-photo" role="img" aria-label="Photo of a tower crane over a building wrapped in green safety netting"></div>
  <div class="about-body">
    <h2>ABOUT</h2>
    <p>It is a long established fact that a reader will be distracted by the readable content of a page when looking at its layout. The point of using Lorem Ipsum is that it has a more-or-less normal distribution of letters,as opposed to using 'Content here, content here', making it look like readable English. Many desktop publishing packages and web page editors now use Lorem Ipsum as their default model text, and a search for 'lorem ipsum' will uncover many web sites still in their infancy. Various versions have evolved over the years, sometimes by accident, sometimes on purpose (injected humour and the like).</p>
    <p>It is a long established fact that a reader will be distracted by the readable content of a page when looking at its layout. The point of using Lorem Ipsum is that it has a more-or-less normal distribution of letters,as opposed to using 'Content here, content here', making it look like readable English. Many desktop publishing packages and web page editors now use Lorem Ipsum as their default model text, and a</p>
  </div>
  <div class="stats">
    <div class="stat blue"><strong>9500</strong><span>Employee worldwide</span></div>
    <div class="stat dark"><strong>€ 1.56 BN</strong><span>Annual Revenue</span></div>
  </div>
</section>

<section class="projects">
  <h2 class="section-title">LATEST PROJECT</h2>
  <div class="container project-grid">
    <div class="project" style="left:0;top:0">
      <div class="project-img" role="img" aria-label="Photo of a blue glass tower with red cranes" style="width:389px;height:483px;background:linear-gradient(180deg,#b9d3ec,#dce8f2 45%,#3d5f95 60%,#2d4470)"></div>
      <h3>Frame Scaffold</h3>
    </div>
    <div class="project" style="left:412px;top:0">
      <div class="project-img" role="img" aria-label="Photo of a building wrapped in shoring scaffolding" style="width:228px;height:214px;background:linear-gradient(180deg,#4e8fd6,#b9c6d1 45%,#7e7a70)"></div>
      <h3>Shoring</h3>
    </div>
    <div class="project" style="left:656px;top:0">
      <div class="project-img" role="img" aria-label="Photo of a crane beside a tall building under a blue sky" style="width:228px;height:214px;background:linear-gradient(180deg,#2f7fd4,#a9cdef 50%,#55575c)"></div>
      <h3>System Scaffold</h3>
    </div>
    <div class="project" style="left:412px;top:268px">
      <div class="project-img" role="img" aria-label="Photo of a timber frame interior" style="width:228px;height:215px;background:linear-gradient(180deg,#8a6a45,#c79a63 55%,#a3764a)"></div>
      <h3>Hydro</h3>
    </div>
    <div class="project" style="left:656px;top:268px">
      <div class="project-img" role="img" aria-label="Photo of a bright empty room with large windows" style="width:228px;height:215px;background:linear-gradient(180deg,#cfd2d4,#eeeeec 60%,#bdbcb8)"></div>
      <h3>Combo Photos</h3>
    </div>
  </div>
  <div class="btn">VIEW MORE</div>
</section>

<section class="testimonials">
  <h2 class="section-title">TESTIMONIAL</h2>
  <div class="quote-card" style="left:162px">
    <div class="avatar" role="img" aria-label="Portrait photo of a client"></div>
    <div class="name">Lorem Ipsum<br>Businessman,NZ</div>
    <div class="mark">“</div>
    <p>It is a long established fact that a reader will be distracted by the readable content of a page when looking at its layout.</p>
  </div>
  <div class="quote-card" style="left:460px">
    <div class="avatar" role="img" aria-label="Portrait photo of a client"></div>
    <div class="name">Lorem Ipsum<br>Businessman,NZ</div>
    <div class="mark">“</div>
    <p>It is a long established fact that a reader will be distracted by the readable content of a page when looking at its layout. distribution of letters,</p>
  </div>
  <div class="quote-card" style="left:763px">
    <div class="avatar" role="img" aria-label="Portrait photo of a client"></div>
    <div class="name">Lorem Ipsum<br>Businessman,NZ</div>
    <div class="mark">“</div>
    <p>It is a long established fact that a reader will be distracted by the readable content of a page when looking at its layout.</p>
  </div>
  <div class="test-dots"><span></span><span class="on"></span><span></span></div>
</section>

<section class="cta">
  <h2>LET BRIGHTRAIL CORVITHANE PROVIDE<br>THE SUPPORT YOUR PROJECT NEEDS.</h2>
  <div class="btn">GET IN TOUCH</div>
</section>

<footer class="footer">
  <div class="brand"><span class="brand-mark"></span>CORVITHANE</div>
  <p class="footer-about">It is a long established fact that a reader will be distracted by the readable content of a page when looking at its layout. The point of using Lorem Ipsum is that it has a more-or-less normal distribution of letters, as opposed to using 'Content here, content here', making</p>
  <div class="footer-col footer-services" style="left:538px">
    <h4>SERVICE</h4>
    <ul>
      <li>Formwork Systems</li>
      <li>Scaffolding Systems</li>
      <li>Civil Engineering Solutions</li>
      <li>Cleaning &amp; Repairs</li>
      <li>Field Services</li>
      <li>Rental Parks &amp; Distribution</li>
    </ul>
  </div>
  <div class="footer-col footer-contact" style="left:817px;width:250px">
    <h4>CONTACT US</h4>
    <ul>
      <li><svg viewBox="0 0 24 24"><path d="M12 2a7 7 0 0 0-7 7c0 5 7 13 7 13s7-8 7-13a7 7 0 0 0-7-7zm0 9.5A2.5 2.5 0 1 1 12 6.5a2.5 2.5 0 0 1 0 5z"/></svg><span>Brightrail Scaffold &amp; Ladders<br>| 4180 Merrow Lane ,NZ</span></li>
      <li><svg viewBox="0 0 24 24"><path d="M6.6 10.8a15 15 0 0 0 6.6 6.6l2.2-2.2a1 1 0 0 1 1-.25 11.4 11.4 0 0 0 3.6.57 1 1 0 0 1 1 1V20a1 1 0 0 1-1 1A17 17 0 0 1 3 4a1 1 0 0 1 1-1h3.5a1 1 0 0 1 1 1c0 1.25.2 2.45.57 3.6a1 1 0 0 1-.25 1z"/></svg><span>555.014.2236</span></li>
      <li><svg viewBox="0 0 24 24"><path d="M2 5h20v14H2zm2 2v.5l8 5 8-5V7z"/></svg><span>info@corvithane.com</span></li>
    </ul>
    <div class="socials" aria-label="Social links"><span></span><span></span><span></span></div>
  </div>
  <div class="copyright">Copyright©2020corvithane. All Rights Reserved.</div>
</footer>

</body>
</html>
```